Business Card Design

I need a business card for a company based in London, UK. I provide garden design, landscaping and maintenance services. The company specialises in modern, urban gardens. It must be horizontal design, white paper and black simple (easy to read) font. The print must be on clear, white surrounding. I like design that use the colours black, yellow, grey and different shades of green. The design must be tidy. It must not be overloaded with decorating. Embodied a small picture of a fragment of garden or plant or leaf in the sun (it must be yellowish and greenish). It would be good if it's "live and energetic". I attached all text and logo that have to appear on the card.

Target Market(s)

architect, property designers, property management companies, large property owners

Industry/Entity Type

Landscaping

Contact Information for Business Card

All the text must be the same as on my old card which I attached.

Requirements
Must have
• modern, simple, tidy, professional look
green, yellow, black colours,
white surrounding,
simple readable black font on clear white surrounding,
a small picture of garden or plant or "sun lights through the tree canopy"
Nice to have
• graduate movement from light green to dark green
Should not have
• old style font,
text must no be placed on pictures or decorations,
red and blue colours,
picture on the reverse

```html
<!DOCTYPE html>
<html lang="en">
<head>
<meta charset="utf-8">
<title>Greenline Gardens – Business Card</title>
<link rel="stylesheet" href="https://fonts.googleapis.com/css2?family=Arimo:wght@400;700&display=swap">
<style>
  :root {
    --page: #e6e6e3;
    --paper: #ffffff;
    --ink: #1a1a1a;
    --grey: #3c3c3c;
    --green-dark: #2f9247;
    --green: #3aaa35;
    --green-mid: #6cb33f;
    --green-lime: #a6ce39;
    --green-light: #a9d47e;
    --yellow: #ffe600;
    --sun: #fffbe0;
  }
  * { box-sizing: border-box; margin: 0; padding: 0; }
  html, body { width: 1200px; height: 1200px; overflow: hidden; }
  body {
    background: var(--page);
    font-family: "Arimo", Arial, sans-serif;
    color: var(--ink);
    position: relative;
  }
  .card {
    position: absolute;
    left: 180px;
    width: 840px;
    height: 552px;
    background: var(--paper);
    overflow: hidden;
    box-shadow: 0 2px 6px rgba(0,0,0,0.12);
  }
  .card--front { top: 38px; background: linear-gradient(160deg, #ffffff 0%, #f4f5f2 100%); }
  .card--back { top: 610px; }

  /* front */
  .sunlit-leaves {
    position: absolute;
    top: 0; right: 0;
    width: 500px; height: 100%;
    background:
      linear-gradient(to right, rgba(255,255,255,1) 0%, rgba(255,255,255,0) 38%),
      radial-gradient(circle at 62% 56%, var(--sun) 0%, #f2f6b8 14%, #cfe774 32%, #94c845 55%, #4f9f3a 82%, #2f7d2e 100%);
  }
  .brand {
    position: absolute;
    left: 48px; top: 100px;
    font-family: "Arimo", Arial, sans-serif;
    font-weight: 400;
    font-size: 38px;
    color: var(--grey);
    letter-spacing: 0.3px;
  }
  .services-line {
    position: absolute;
    left: 50px; top: 154px;
    font-size: 23px;
    letter-spacing: 0.4px;
    color: var(--grey);
  }
  .services-line .s1 { color: var(--green-dark); }
  .services-line .s2 { color: var(--green-lime); }
  .services-line .sep { color: var(--green-mid); margin: 0 6px; }

  .contact-name {
    position: absolute;
    left: 44px; top: 258px;
    width: 222px;
    font-weight: 700;
    font-size: 21px;
    letter-spacing: 0.5px;
    padding-bottom: 4px;
    border-bottom: 2px solid var(--green-dark);
  }
  .contact-list {
    position: absolute;
    left: 44px; top: 302px;
    list-style: none;
  }
  .contact-list li {
    display: flex; align-items: center;
    height: 39.5px;
    font-size: 19px;
  }
  .contact-list svg { width: 28px; height: 28px; margin-right: 6px; flex: none; }
  .web-pill {
    position: absolute;
    left: 46px; top: 473px;
    width: 400px; height: 35px;
    border-radius: 10px;
    background: var(--green-lime);
    color: #fff;
    font-size: 22px;
    letter-spacing: 0.3px;
    display: flex; align-items: center; justify-content: center;
  }

  /* back */
  .service {
    position: absolute;
    left: 48px;
    padding-left: 30px;
    width: 760px;
  }
  .service__bar {
    position: absolute;
    left: 0; top: 0;
    width: 12px; height: 76px;
    clip-path: polygon(0 0, 70% 0, 70% 38%, 100% 50%, 70% 62%, 70% 100%, 0 100%);
  }
  .service__title { font-size: 27px; font-weight: 400; line-height: 34px; }
  .service__text { font-size: 16px; line-height: 26px; margin-top: 4px; }
  .service--design { top: 42px; }
  .service--maint { top: 138px; }
  .service--grounds { top: 232px; }
  .service--hard { top: 344px; }
  .service--water { top: 440px; }
  .service--design .service__bar { background: var(--green-dark); }
  .service--maint .service__bar { background: var(--green-lime); }
  .service--grounds .service__bar { background: var(--yellow); }
  .service--hard .service__bar { background: var(--green-light); }
  .service--water .service__bar { background: var(--green); }
</style>
</head>
<body>

<section class="card card--front">
  <div class="sunlit-leaves" role="img" aria-label="Close-up of green leaves with sunlight shining through the canopy"></div>

  <p class="brand">Greenline Gardens</p>
  <p class="services-line"><span class="s1">DESIGN</span><span class="sep">|</span><span class="s2">LANDSCAPING</span><span class="sep">|</span><span class="s3">MAINTENANCE</span></p>

  <h2 class="contact-name">DANIEL MARSH</h2>
  <ul class="contact-list">
    <li>
      <svg viewBox="0 0 28 28" aria-hidden="true"><path d="M3 25 C3 10 12 3 25 3 C25 16 18 25 3 25Z" fill="#3aaa35"/><path d="M14 7a4.5 4.5 0 0 0-4.5 4.5c0 3.4 4.5 8 4.5 8s4.5-4.6 4.5-8A4.5 4.5 0 0 0 14 7z" fill="#fff"/><circle cx="14" cy="11.5" r="1.7" fill="#3aaa35"/></svg>
      27 Mill Lane,Ashford,TW15 2QR
    </li>
    <li>
      <svg viewBox="0 0 28 28" aria-hidden="true"><path d="M3 25 C3 10 12 3 25 3 C25 16 18 25 3 25Z" fill="#3aaa35"/><path d="M8 11c2-3 10-3 12 0l-2 2-2-1v-1h-4v1l-2 1z M9 14h10l1 5H8z" fill="#fff"/></svg>
      02084517296
    </li>
    <li>
      <svg viewBox="0 0 28 28" aria-hidden="true"><path d="M3 25 C3 10 12 3 25 3 C25 16 18 25 3 25Z" fill="#3aaa35"/><rect x="10" y="7" width="8" height="14" rx="1.5" fill="#fff"/><rect x="11.5" y="9" width="5" height="7" fill="#3aaa35"/></svg>
      07912345608
    </li>
    <li>
      <svg viewBox="0 0 28 28" aria-hidden="true"><path d="M3 25 C3 10 12 3 25 3 C25 16 18 25 3 25Z" fill="#3aaa35"/><text x="14" y="18.5" text-anchor="middle" font-family="Arimo, Arial, sans-serif" font-weight="700" font-size="12" fill="#fff">@</text></svg>
      info@greenline-gardens.co.uk
    </li>
  </ul>
  <div class="web-pill">www.greenline-gardens.co.uk</div>
</section>

<section class="card card--back">
  <div class="service service--design">
    <span class="service__bar"></span>
    <h3 class="service__title">Garden Design</h3>
    <p class="service__text">All styles;hand-drawn &amp; CAD, detailed mapping.underground service tracing soil analysis.</p>
  </div>
  <div class="service service--maint">
    <span class="service__bar"></span>
    <h3 class="service__title">Garden Maintenance</h3>
    <p class="service__text">lawn care programs,improving the soil,plant health issues,clearance tree husbandry.</p>
  </div>
  <div class="service service--grounds">
    <span class="service__bar"></span>
    <h3 class="service__title">Grounds Maintenance</h3>
    <p class="service__text">algae,moss &amp; pest control,drainage improvements; green areas,car parks playgrounds,<br>Garden Revival</p>
  </div>
  <div class="service service--hard">
    <span class="service__bar"></span>
    <h3 class="service__title">Patios,Fences,Decking</h3>
    <p class="service__text">railings,walls,driveways,summerhouses;hard &amp; soft wood,natural stone,slabs.</p>
  </div>
  <div class="service service--water">
    <span class="service__bar"></span>
    <h3 class="service__title">Ponds,Irrigation,Lighting</h3>
    <p class="service__text">rockeries,water features;timers,drip &amp; sprinkler systems;installation &amp; maintenance.</p>
  </div>
</section>

</body>
</html>
```